Asia based real estate financing firm needs and AWESOME design for a biz card -Harbor Lending Circle

Looking for a stylish, & corporate-looking business card for a real estate financing brokerage firm in Asia, offering global mortgage loans. I uploaded our current logos. We would like to add a splash of color (perhaps the house icon) or any other suggestions are open. For the winning designer, we have a lot of work! Thanks and best of luck!

Target Market(s)

Real estate investors globally. We want to look more like a BANK and NOT a real estate company. Please don't play up on a "house" design.

Industry/Entity Type

Banking

Contact Information for Business Card

Harbor Lending Circle
Peter Wilks
Co-Founder | Partner

14 Cassia Lane, Suite 310
Singapore 047219
www.hlc-example.asia
peterwilks@hlc-example.asia
+65 555-0142
WeChat: peterwilks

Colors

Designer to choose colors to be used in the design.

Requirements
Must have
• Must have the standard business requirements for a card; name, address, email, etc
• Can be horizontal or vertical.
Nice to have
• It would be great to see some sort of variation to the logo with a pop of color. Red is good as we're in Asia, however, other options work as well.
• Our tag line is - Lending without limits. It doesn't have to be on the card but might be nice.
• I'd like to start seeing our tagline within the cards as well. - Lending without limits.
• Also, please add our location. The location for this card is Singapore so perhaps it can be highlighted or emphasised in some way.
• Singapore | Hong Kong | Shanghai | Manila
• As we will soon open an office in Shanghai, having an option for both languages would be great.
Should not have
• I'm exceited and open to your creativity ... knock it out of the park!

```html
<!DOCTYPE html>
<html lang="en">
<head>
<meta charset="utf-8">
<title>Harbor Lending Circle – Business Card</title>
<link rel="stylesheet" href="https://fonts.googleapis.com/css2?family=Cinzel:wght@400;500&family=Roboto:wght@300;400;700&display=swap">
<style>
  :root {
    --backdrop: #1c1c1d;
    --paper: #f4f3f1;
    --paper-shade: #ecebe8;
    --pattern-tint: #efe4e3;
    --brand-red: #c2161c;
    --ink: #111111;
    --ink-soft: #4a4a4a;
    --ink-muted: #6d6d6d;
    --white: #ffffff;
  }
  * { box-sizing: border-box; margin: 0; padding: 0; }
  html, body {
    width: 1200px;
    height: 1063px;
    overflow: hidden;
    background: var(--backdrop);
  }
  .stage {
    width: 1200px;
    height: 1063px;
    display: flex;
    flex-direction: column;
    align-items: center;
    justify-content: center;
    gap: 40px;
  }
  .card {
    position: relative;
    width: 840px;
    height: 480px;
    background: var(--paper);
    overflow: hidden;
  }

  /* Front */
  .card-front__pattern {
    position: absolute;
    inset: 0;
    background: linear-gradient(135deg, var(--paper) 0%, var(--pattern-tint) 50%, var(--paper) 100%);
  }
  .brand {
    position: absolute;
    left: 0;
    right: 0;
    top: 170px;
    display: flex;
    align-items: center;
    justify-content: center;
    gap: 22px;
  }
  .brand__square {
    width: 22px;
    height: 22px;
    background: var(--brand-red);
  }
  .brand__name {
    font-family: "Cinzel", serif;
    font-weight: 400;
    font-size: 52px;
    letter-spacing: 2px;
    color: var(--ink);
    white-space: nowrap;
  }
  .tagline-band {
    position: absolute;
    left: 0;
    right: 0;
    top: 372px;
    height: 52px;
    background: var(--brand-red);
    display: flex;
    align-items: center;
    padding-left: 80px;
  }
  .tagline {
    font-family: "Cinzel", serif;
    font-weight: 400;
    font-size: 17px;
    letter-spacing: 2.5px;
    color: var(--white);
    white-space: nowrap;
  }

  /* Back */
  .card-back {
    background: linear-gradient(160deg, var(--paper) 0%, var(--paper-shade) 100%);
  }
  .contact-block {
    position: absolute;
    left: 330px;
    top: 92px;
    font-family: "Roboto", sans-serif;
  }
  .contact-block__mark {
    width: 18px;
    height: 18px;
    background: var(--brand-red);
    margin-bottom: 14px;
  }
  .person__name {
    font-weight: 700;
    font-size: 25px;
    letter-spacing: 0.5px;
    color: var(--brand-red);
    text-transform: uppercase;
    line-height: 1.1;
  }
  .person__title {
    font-weight: 400;
    font-size: 18px;
    color: var(--ink-soft);
    margin-top: 3px;
  }
  .divider {
    width: 44px;
    height: 2px;
    background: var(--brand-red);
    margin: 22px 0;
  }
  .address {
    font-weight: 300;
    font-size: 16px;
    line-height: 1.4;
    color: var(--ink-muted);
    font-style: normal;
  }
  .contact-list {
    list-style: none;
    font-weight: 300;
    font-size: 16px;
    line-height: 1.4;
    color: var(--ink-muted);
  }
  .contact-list__item {
    display: flex;
    align-items: center;
    gap: 7px;
    white-space: nowrap;
  }
  .contact-list__icon {
    width: 13px;
    height: 13px;
    flex: none;
  }
</style>
</head>
<body>
<main class="stage">

  <section class="card card-front" aria-label="Card front">
    <div class="card-front__pattern" role="img" aria-label="Faint repeating small brand-mark pattern in pale red on white"></div>
    <div class="brand">
      <span class="brand__square" aria-hidden="true"></span>
      <span class="brand__name">Harbor Lending Circle</span>
    </div>
    <div class="tagline-band">
      <span class="tagline">LENDING WITHOUT LIMITS.</span>
    </div>
  </section>

  <section class="card card-back" aria-label="Card back">
    <div class="contact-block">
      <div class="contact-block__mark" aria-hidden="true"></div>
      <h1 class="person__name">Peter Wilks</h1>
      <p class="person__title">Co-Founder/Partner</p>

      <div class="divider"></div>

      <address class="address">
        14 Cassia Lane, Suite 310<br>
        Singapore 047219
      </address>

      <div class="divider"></div>

      <ul class="contact-list">
        <li class="contact-list__item">
          <svg class="contact-list__icon" viewBox="0 0 16 16" aria-hidden="true">
            <path fill="#c2161c" d="M3.6 1.5l2.3 2.7-1.3 1.6c.8 1.9 2.1 3.3 4 4.2l1.6-1.3 2.7 2.3-1.3 2.4C6.6 13.6 2.3 9.3 1.2 2.8z"/>
          </svg>
          <span>+65 555-0142</span>
        </li>
        <li class="contact-list__item">
          <svg class="contact-list__icon" viewBox="0 0 16 16" aria-hidden="true">
            <rect x="1" y="3" width="14" height="10" fill="#c2161c"/>
            <path d="M1.5 3.5L8 9l6.5-5.5" fill="none" stroke="#f4f3f1" stroke-width="1.3"/>
          </svg>
          <span>peterwilks@hlc-example.asia</span>
        </li>
        <li class="contact-list__item">
          <svg class="contact-list__icon" viewBox="0 0 16 16" aria-hidden="true">
            <circle cx="8" cy="8" r="7" fill="#c2161c"/>
            <ellipse cx="8" cy="8" rx="3" ry="7" fill="none" stroke="#f4f3f1" stroke-width="1"/>
            <path d="M1 8h14" stroke="#f4f3f1" stroke-width="1"/>
          </svg>
          <span>www.hlc-example.asia</span>
        </li>
        <li class="contact-list__item">
          <svg class="contact-list__icon" viewBox="0 0 16 16" aria-hidden="true">
            <rect x="1.5" y="1.5" width="13" height="13" fill="#c2161c"/>
          </svg>
          <span>peterwilks</span>
        </li>
      </ul>
    </div>
  </section>

</main>
</body>
</html>
```